Plastic Seasoning Bottle Design Label

I am looking to get a label design that's going on plastic seasoning bottles. My company which deals with seasons/spices. My company sells healthy all natural seasons so I would like the label to have a design of natural. I also would like a hot pepper on there showing it's hot and also other red indentations like red fire or something that shows it's very hot !!!
The company name is Brisk Meadow Harvest which I would like in light green letters.
There are six different seasonings favors which are:
Barbecue
Garlic
Lemon
Chili
Poultry/Meat
Seafood

The label size: 190.00mm x 111.00mm

Thanks

I would like for the colors to be:
Green
Light Green
Red ( For Hot )
White
Seafood
All of them will be hot as it will show on the label.

Hello, Please include on the labels pictures of the foods associated with the seasoning. Example: Seafood= Fish,lobster,clams,shrimp,scallops,eel,octopus,squid and muscles which will show that it's also very hot. As for seasonings like the Lemon you could just put pictures of lemons which are showing also that there hot as all of the seasoning are hot also. Garlic would be the same as the lemon with just picture also showing it's very hot. Meat would show different kinds of beef such as steak,hamburgers. Also chicken and ham which will show that it's also very hot. Barbecue and Chili you can feel free to show different ideas on that as they will also show that they are very hot as all of them are. The label size is 190.00mm x 111.00mm If you need more time to work on this project please feel free to let me know as I have no problem extending the dead line. Thanks

Hello, In the last update I mentioned Ham as I met to put Ribs not Ham. Thanks

Hello, The budget has been increased. It's now 201.00

Hello, At the end of the company name I would like to have a small TM at the end of the company name as the the has a trade mark on it. Thanks

Industry/Entity Type

Plastic

Font styles to use
Serif
Sans Serif
Decorative
Script
Other font styles liked:
• Georgia,Italic,Bold

```html
<!DOCTYPE html>
<html lang="en">
<head>
<meta charset="utf-8">
<title>Brisk Meadow Harvest – Seasoning Labels</title>
<link rel="stylesheet" href="https://fonts.googleapis.com/css2?family=Gelasio:ital,wght@0,700;1,700&family=Tinos:wght@700&display=swap">
<style>
  :root{
    --forest:#0f6b35;
    --stripe:#1f8a3e;
    --leaf:#8dc63f;
    --lime:#c8df1f;
    --cream:#f6f3b0;
    --chili:#c1272d;
    --flame-red:#e2262a;
    --flame-orange:#f7931e;
    --flame-yellow:#ffd51c;
    --white:#ffffff;
    --gold:#c9b24a;
    --lemon:#ffe600;
  }
  *{margin:0;padding:0;box-sizing:border-box}
  html,body{width:1200px;height:1000px;overflow:hidden;background:var(--white)}
  .sheet{position:relative;width:1200px;height:1000px}
  .defs{position:absolute;width:0;height:0}

  .label{position:absolute;width:180px;height:312px;overflow:hidden;
    background:repeating-linear-gradient(90deg,var(--forest) 0 5px,var(--stripe) 5px 8px);}
  .label__band{position:absolute;left:28px;top:0;width:124px;height:278px;
    background:linear-gradient(180deg,var(--leaf) 0%,#a5d13a 40%,var(--lime) 100%);}
  .label__badge{position:absolute;left:0;top:0;width:180px;height:312px}

  .brand{position:absolute;left:52px;top:12px;width:76px;height:76px;border-radius:50%;
    background:linear-gradient(180deg,var(--leaf),var(--stripe));display:flex;align-items:center;justify-content:center}
  .brand__disc{width:64px;height:64px;border-radius:50%;background:var(--white);
    display:flex;align-items:center;justify-content:center;text-align:center;
    font-family:"Gelasio",Georgia,serif;font-weight:700;color:var(--leaf);font-size:10.5px;line-height:1.05}

  .art{position:absolute;left:12px;top:82px;width:156px;height:82px;border-radius:40% 40% 10px 10px;
    background:radial-gradient(ellipse at 50% 40%,var(--art-core) 0 38%,var(--flame-orange) 62%,var(--flame-red) 82%,transparent 100%)}

  .flavor{position:absolute;left:12px;top:158px;width:156px;height:38px;border:2px solid var(--cream);border-radius:3px;
    background:linear-gradient(90deg,var(--lime) 0%,#9fcf2c 55%,var(--stripe) 100%);
    display:flex;align-items:center;justify-content:center;
    font-family:"Tinos","Times New Roman",serif;font-weight:700;font-size:27px;color:var(--chili);letter-spacing:.5px}
  .flavor--small{font-size:19px;letter-spacing:0}
  .flavor--lemon{color:var(--lemon);background:linear-gradient(90deg,#9fcf2c,var(--stripe))}
  .flavor--garlic{color:var(--gold);background:var(--forest)}
  .flavor--bbq{color:var(--flame-red);background:var(--lime)}

  .flames{position:absolute;left:0;top:246px;width:180px;height:32px;
    background:linear-gradient(0deg,var(--flame-yellow) 0%,var(--flame-orange) 45%,var(--flame-red) 75%,transparent 100%)}
  .footer{position:absolute;left:0;top:278px;width:180px;height:34px;background:var(--leaf);
    display:flex;align-items:center;justify-content:center;
    font-family:"Gelasio",Georgia,serif;font-style:italic;font-weight:700;font-size:14px;color:var(--white)}
  .seasoning-text{font-family:"Tinos","Times New Roman",serif;font-size:12px;fill:var(--white);letter-spacing:.5px}
</style>
</head>
<body>
<div class="sheet">
  <svg class="defs" aria-hidden="true">
    <defs>
      <linearGradient id="badgeFill" x1="0" y1="0" x2="0" y2="1">
        <stop offset="0" stop-color="#c8df1f"/>
        <stop offset="1" stop-color="#0f7a3a"/>
      </linearGradient>
      <path id="seasoningArc" d="M50 206 A40 40 0 0 0 130 206"/>
    </defs>
  </svg>

  <!-- Seafood -->
  <div class="label" style="left:68px;top:123px">
    <div class="label__band"></div>
    <svg class="label__badge" viewBox="0 0 180 312"><circle cx="90" cy="200" r="46" fill="url(#badgeFill)"/><text class="seasoning-text"><textPath href="#seasoningArc" startOffset="50%" text-anchor="middle">SEASONING</textPath></text></svg>
    <div class="art" style="--art-core:#d84a2a" role="img" aria-label="Lobster, shrimp, fish and shellfish in flames"></div>
    <div class="brand"><div class="brand__disc">Brisk<br>Meadow<br>Harvest™</div></div>
    <div class="flavor">SEAFOOD</div>
    <div class="flames" role="img" aria-label="Row of flames"></div>
    <div class="footer">All Nature</div>
  </div>

  <!-- Poultry/Meat -->
  <div class="label" style="left:275px;top:123px">
    <div class="label__band"></div>
    <svg class="label__badge" viewBox="0 0 180 312"><circle cx="90" cy="200" r="46" fill="url(#badgeFill)"/><text class="seasoning-text"><textPath href="#seasoningArc" startOffset="50%" text-anchor="middle">SEASONING</textPath></text></svg>
    <div class="art" style="--art-core:#e8a8a8" role="img" aria-label="Chicken, steak and ribs in flames"></div>
    <div class="brand"><div class="brand__disc">Brisk<br>Meadow<br>Harvest™</div></div>
    <div class="flavor flavor--small">POULTRY/MEAT</div>
    <div class="flames" role="img" aria-label="Row of flames"></div>
    <div class="footer">All Nature</div>
  </div>

  <!-- Lemon -->
  <div class="label" style="left:483px;top:123px">
    <div class="label__band"></div>
    <svg class="label__badge" viewBox="0 0 180 312"><circle cx="90" cy="200" r="46" fill="url(#badgeFill)"/><text class="seasoning-text"><textPath href="#seasoningArc" startOffset="50%" text-anchor="middle">SEASONING</textPath></text></svg>
    <div class="art" style="--art-core:#f7c21a" role="img" aria-label="Whole and sliced lemons in flames"></div>
    <div class="brand"><div class="brand__disc">Brisk<br>Meadow<br>Harvest™</div></div>
    <div class="flavor flavor--lemon">LEMON</div>
    <div class="flames" role="img" aria-label="Row of flames"></div>
    <div class="footer">All Nature</div>
  </div>

  <!-- Barbecue -->
  <div class="label" style="left:698px;top:123px">
    <div class="label__band"></div>
    <svg class="label__badge" viewBox="0 0 180 312"><circle cx="90" cy="200" r="46" fill="url(#badgeFill)"/><text class="seasoning-text"><textPath href="#seasoningArc" startOffset="50%" text-anchor="middle">SEASONING</textPath></text></svg>
    <div class="art" style="--art-core:#ffd51c" role="img" aria-label="Large fire flames"></div>
    <div class="brand"><div class="brand__disc">Brisk<br>Meadow<br>Harvest™</div></div>
    <div class="flavor flavor--bbq">BARBECUE</div>
    <div class="flames" role="img" aria-label="Row of flames"></div>
    <div class="footer">All Nature</div>
  </div>

  <!-- Garlic -->
  <div class="label" style="left:922px;top:123px">
    <div class="label__band"></div>
    <svg class="label__badge" viewBox="0 0 180 312"><circle cx="90" cy="200" r="46" fill="url(#badgeFill)"/><text class="seasoning-text"><textPath href="#seasoningArc" startOffset="50%" text-anchor="middle">SEASONING</textPath></text></svg>
    <div class="art" style="--art-core:#eeeae0" role="img" aria-label="Garlic bulbs and cloves in flames"></div>
    <div class="brand"><div class="brand__disc">Brisk<br>Meadow<br>Harvest™</div></div>
    <div class="flavor flavor--garlic">GARLIC</div>
    <div class="flames" role="img" aria-label="Row of flames"></div>
    <div class="footer">All Nature</div>
  </div>

  <!-- Chili -->
  <div class="label" style="left:480px;top:530px">
    <div class="label__band"></div>
    <svg class="label__badge" viewBox="0 0 180 312"><circle cx="90" cy="200" r="46" fill="url(#badgeFill)"/><text class="seasoning-text"><textPath href="#seasoningArc" startOffset="50%" text-anchor="middle">SEASONING</textPath></text></svg>
    <div class="art" style="--art-core:#c8161d" role="img" aria-label="Red chili peppers in flames"></div>
    <div class="brand"><div class="brand__disc">Brisk<br>Meadow<br>Harvest™</div></div>
    <div class="flavor">CHILI</div>
    <div class="flames" role="img" aria-label="Row of flames"></div>
    <div class="footer">All Nature</div>
  </div>
</div>
</body>
</html>
```